Website - TRSC

Having reviewed the designs received so far, no one design is meeting the client’s needs. The client has identified desirable elements from the designs submitted, which we want to see brought together.
Header
It is important that the logo is given space – ie is not overlayed on an image, nor with a short fade into an image. A gradual fade into the header image is acceptable.
Background
While an image background is acceptable, this should only be visible on the left and right borders, it should not be used underneath the main content area.
Main menu
The main menu should be a cohesive bar across the page – not separate buttons. Buttons that are connected together within a bar are acceptable. Menu items should be separated using a pipe ( | ), or by being framed (as long as the framing sits within a bar). Menu item should change colour to indicate the page you are on.
Left Hand Boxes
There should be consistency in colouring through these. It is acceptable to use one colour for the heading , and another for the content area. It is not acceptable for each box to have a different scheme. This applies to the right hand feature boxes as well.
Colouring
We want to keep this simple. Please use colours from the logo, feel free to add complimentary colours but keep the palette limited. If shading is used with any of the colours be careful to not move it too far from the original colour. The yellow does not look good with too much of a grey shade.
Feature Boxes
The two feature boxes on the home page (Browse Homes and Local Knowledge) need to stand out. An option is to ensure that the associated link button uses one of the brighter colours in the palette.
_____________________________________________________
Note: I have attached the newly design logo to the brief. It is important that colours from the logo are used on the design. Blue denotes water and the yellow denotes sand and sun.
I'd like to see the feel of the logo reflected in the site.
______________________________________________
Tui Crib and Seaside Cottages is rebuilding its website – www.tuicribandseasidecottages.co.nz.
We require the design of two pages:
• Home
• House detail page (pgs 3-5 of the attachment).
We have specified a layout for the site (attached).
The contextual information below provides the feeling the site needs to convey.
If further information is required please contact us.
CONTEXT/BACKGROUND
Tui Crib and Seaside Cottages (TRSC) has been in business now for over 11 years and is due for a facelift. We have about 40 – 60 houses available during the peak summer period – about 50% are permanent holiday homes, the balance are local family homes being rented out while they are away on holiday.
We are currently located in Marram Sands – but with the national name have the ability and goal to expand into other areas of New Zealand – so any logo etc has to have the ability to represent other holiday destinations within NZ. Bear in mind that our primary location is Marram at the moment.
Our key market is families going on holiday – looking for a holiday home to book (currently an Marram Sands holiday)
Secondary market is couples or mature groups looking at having some R&R or business groups having some team building/ management meetings away from the busy office surroundings.
We manage ALL the properties so are a great source of information on what holiday home is best suited to each family and “things to do” in the area – i.e. other activities.
Our main focus is to be the best “holiday home” - accommodation provider in whatever location TRSC is representing. We want to be seen as having a good supply of great homes, providing a great service as well as being a good source of local knowledge.
We want to be seen as PROFESSIONALS in the holiday rental business (from occupants and owners).
TRUST – we want people to be able to trust us by listing their property with us (owners) and confidently booking accommodation through us (occupants).
TAGLINE SUGGESTIONS
Key motif – “TRSC, your door to a fine escape!” The “key”, of course is a double play on the house key you get. But it is also extendible to other aspect of the experience we offer. For example the phrase: “getting the key to the city” is applicable to us – we give them the key to Marram…(or whatever location we are marketing in the future). Potentially we may consider promotional merchandise around this, eg promo key rings etc.
Some key words/phrases that our business represents are:
• ‘Our place is your place’
• Connect – connecting families to holiday homes and the area – at the moment only Marram.
• Local – local people looking after your needs – “our place is your place – so make yourself at home!”
• Link – we are the link to a real kiwi holiday experience.
• Holiday - R&R – rest and recreation
More specific to Marram:
• Safe Natural playground – beach, bush, fishing, outdoor activities – creating real family memories.
Website:
• Need to focus on the Local and Personal property management factors in website to differentiate us from other nationwide listing sites – contact us and we can help you find the right accommodation and save you time
• Play on the HOLIDAYMAKER experience more, including giving prominence to visitor deals, become a local etc, differentiating us from other local holiday home rental businesses.
• Real – real people, real places, real experiences.
• User friendly, informative, professional with a personal touch/feel, to encourage the holiday feeling.
Having reviewed the designs received so far, no one design is meetingthe client’s needs. The client has identified desirable elements from thedesigns submitted, which we want to see brought together.
Header
It is important that the logo is given space – ie is not overlayed on animage, nor with a short fade into an image. A gradual fade into the headerimage is acceptable.
Background
While an image background is acceptable, this should only be visible onthe left and right borders, it should not be used underneath the main contentarea.
Main menu
The main menu should be a cohesive bar across the page – not separatebuttons. Buttons that are connected together within a bar are acceptable.Menu items should be separated using a pipe ( | ), or by being framed (as longas the framing sits within a bar). Menu item should change colour to indicatethe page you are on.
Left Hand Boxes
There should be consistency in colouring through these. It isacceptable to use one colour for the heading , and another for the contentarea. It is not acceptable for each box to have a different scheme. Thisapplies to the right hand feature boxes as well.
Colouring
We want to keep this simple. Please use colours from the logo,feel free to add complimentary colours but keep the palette limited. Ifshading is used with any of the colours be careful to not move it too far fromthe original colour. The yellow does not look good with too much of agrey shade.
Feature Boxes
The two feature boxes on the home page (Browse Homes and LocalKnowledge) need to stand out. An option is to ensure that the associated linkbutton uses one of the brighter colours in the palette.

```html
<!DOCTYPE html>
<html lang="en">
<head>
<meta charset="utf-8">
<title>Tui Crib &amp; Seaside Cottages</title>
<link rel="stylesheet" href="https://fonts.googleapis.com/css2?family=Oswald:wght@400;500&family=Arimo:wght@400;700&display=swap">
<style>
:root{
  --sea:#0b6cbf;
  --sea-deep:#0a5ea9;
  --nav-top:#2394e6;
  --nav-bottom:#0865b8;
  --sun:#ffd21f;
  --sun-deep:#f5b400;
  --sand-pale:#fff7c6;
  --sky-pale:#e4f1fc;
  --ink:#333;
  --text:#4a4a4a;
  --link:#0a6fc4;
  --panel:#f6f6f6;
  --charcoal:#2f2f2f;
  --alert:#e0201b;
  --orange:#f7a500;
}
*{box-sizing:border-box;margin:0;padding:0}
html,body{width:1104px;height:1200px;overflow:hidden}
body{background:var(--sea);font-family:Arimo,Arial,sans-serif;color:var(--text)}
.stage{position:absolute;left:0;top:0;width:1084px;height:1178px;transform-origin:0 0;transform:scale(1.0185,1.0187)}
.abs{position:absolute}
.page-column{left:40px;top:0;width:1008px;height:1178px;background:#fff}
.site-footer{left:40px;top:1128px;width:1008px;height:50px;background:linear-gradient(#cfe5f7,#eef6fd 40%,#fff);border-top:2px solid #b9d8f2}
.footer-links{left:0;top:1144px;width:1084px;text-align:center;font-size:15px;word-spacing:2px}
.footer-links a{color:var(--link);text-decoration:none;margin:0 9px}

.hero{left:59px;top:0;width:970px;height:266px;background:linear-gradient(100deg,#0f83c8 0%,#1aa0d8 35%,#2cb1e0 55%,#3c8c9a 72%,#557e4a 85%,#6d8a4e 100%)}
.brand-card{left:96px;top:65px;width:259px;height:155px;background:#fff;border:2px solid #c9dff0;border-radius:4px;display:flex;flex-direction:column;align-items:center;justify-content:center;gap:12px}
.brand-dot{width:46px;height:46px;border-radius:50%;background:var(--sun)}
.brand-name{font-family:Oswald,sans-serif;font-size:21px;color:#3a3a3a;letter-spacing:-.2px}

.main-nav{left:59px;top:265px;width:970px;height:41px;background:linear-gradient(var(--nav-top),var(--nav-bottom));border-top:2px solid #5fb3f0}
.nav-item{position:absolute;top:8px;font-family:Oswald,sans-serif;font-size:17px;color:#fff;white-space:nowrap}
.nav-item.is-current{top:-10px;height:48px;padding:17px 9px 0;background:linear-gradient(#ffe24a,var(--sun-deep));color:#222;border-radius:3px 3px 0 0}
.nav-peak{left:336px;top:257px}

.box{left:59px;width:263px;border-radius:5px;overflow:hidden}
.box-title{height:37px;padding:5px 9px;font-family:Oswald,sans-serif;font-size:22px;line-height:26px}
.quick-search{top:316px;height:249px;background:var(--sand-pale);border:1px solid #f0d560}
.quick-search .box-title{background:linear-gradient(#ffe030,var(--sun-deep));color:#222}
.field-label{position:absolute;font-size:13px;color:#222}
.select{position:absolute;height:28px;border:1px solid #bdbdbd;border-radius:3px;background:linear-gradient(#fff,#e6e6e6)}
.select::after{content:"";position:absolute;right:6px;top:7px;width:14px;height:13px;background:#ddd;border:1px solid #999;clip-path:none}
.select i{position:absolute;right:10px;top:12px;width:0;height:0;border-left:4px solid transparent;border-right:4px solid transparent;border-top:6px solid #222;z-index:1}
.text-input{position:absolute;height:29px;border:1px solid #bdbdbd;border-radius:3px;background:linear-gradient(#fff,#ececec);font-size:11px;color:#777;padding:8px 6px}
.btn-dark{position:absolute;background:linear-gradient(#6a6a6a,#1f1f1f);color:#fff;font-family:Arimo,sans-serif;font-weight:700;font-size:14px;text-align:center;border-radius:3px}
.small-link{position:absolute;color:var(--link);font-size:12px}

.keep-in-touch{top:585px;height:217px;background:var(--sky-pale);border:1px solid #6fb2e6}
.keep-in-touch .box-title{background:linear-gradient(#1f8ee2,var(--sea-deep));color:#fff}
.intro{position:absolute;left:0;top:42px;width:263px;text-align:center;font-size:14.5px;line-height:22px;color:#444}
.social-btn{position:absolute;left:8px;top:175px;width:104px;height:31px;background:linear-gradient(#4a6aa8,#2c4a86);color:#fff;font-size:13px;padding:8px 7px;border-radius:3px}
.social-btn span{position:absolute;right:6px;top:6px;width:18px;height:18px;background:#fff;opacity:.25}

.deals{top:825px;height:216px;background:linear-gradient(#fff,#ececec);border:1px solid #555}
.deals .box-title{background:linear-gradient(#5c5c5c,var(--charcoal));color:#fff}
.deal-photo{position:absolute;left:6px;top:43px;width:119px;height:130px;background:linear-gradient(#d9eefb,#9fd0ef 55%,#f3efe7 80%,#e8e2d4)}
.deal-copy{position:absolute;left:134px;top:40px;width:126px;font-size:13.5px;line-height:22px;color:#333}

.share-bar{left:59px;top:1055px;width:263px;height:53px;border:1px solid #999;background:#fff}
.share-icon{position:absolute;top:6px}
.share-label{position:absolute;left:179px;top:18px;font-size:13.5px;color:#222}

.content{left:343px;top:316px;width:686px;height:792px;background:var(--panel);border:1px solid #e4e4e4}
.welcome{left:363px;top:336px;font-family:Oswald,sans-serif;font-size:19px;color:var(--ink);font-weight:400}
.copy{font-size:12.6px;line-height:16.6px;text-align:justify;color:#444}
.shortlist{left:878px;top:324px;width:139px;height:85px;border-radius:4px;background:linear-gradient(#ffc21a,var(--orange));border:1px solid #d88a00;text-align:center;font-weight:700;font-size:26px;line-height:30px;color:#fff;padding-top:11px;text-shadow:0 0 2px #7a4a00,1px 1px 1px #6b3d00}
.help{left:878px;top:419px;width:139px;height:206px;border-radius:5px;background:linear-gradient(#e9f5fd,#fff);border:2px solid #c8e2f5;text-align:center}
.help h3{font-size:26px;color:#1689dd;margin-top:6px}
.help p{font-size:14.5px;font-weight:700;line-height:21px;color:#333;margin-top:6px;letter-spacing:.3px}
.help .phone{color:var(--alert);font-size:15px;margin-top:8px}
.cta{left:343px;top:785px;width:686px;text-align:center;font-weight:700;font-size:22.5px;line-height:36px;color:var(--ink)}
.cta a{color:var(--link);text-decoration:none}
.feature-photo{top:872px;height:174px;border:1px solid #888}
.feature-label{top:1059px;font-size:17px;color:#444;text-align:center}
</style>
</head>
<body>
<div class="stage">
  <div class="abs page-column"></div>

  <header>
    <div class="abs hero" role="img" aria-label="Aerial photo of a rocky headland, turquoise sea and a green coastal settlement"></div>
    <div class="abs brand-card">
      <div class="brand-dot"></div>
      <div class="brand-name">Tui Crib &amp; Seaside Cottages</div>
    </div>
    <svg class="abs nav-peak" width="170" height="10" viewBox="0 0 170 10"><path d="M0 9 L20 1 L40 9 Z M130 9 L150 1 L170 9 Z" fill="#f5b400"/></svg>
    <nav class="abs main-nav">
      <span class="nav-item" style="left:23px">Home</span>
      <span class="nav-item" style="left:88px">Browse Homes</span>
      <span class="nav-item" style="left:212px">Packages</span>
      <span class="nav-item is-current" style="left:296px">Local Knowledge</span>
      <span class="nav-item" style="left:446px">About us</span>
      <span class="nav-item" style="left:532px">Contact us</span>
      <span class="nav-item" style="left:631px">List your Homes</span>
    </nav>
  </header>

  <aside>
    <section class="abs box quick-search">
      <h2 class="box-title">Quick Search</h2>
      <span class="field-label" style="left:9px;top:45px">No. Of Guests Beach</span>
      <div class="select" style="left:8px;top:63px;width:246px"><i></i></div>
      <span class="field-label" style="left:9px;top:104px">Nightly Rate</span>
      <div class="select" style="left:8px;top:124px;width:117px"><i></i></div>
      <span class="field-label" style="left:134px;top:131px">to</span>
      <div class="select" style="left:158px;top:124px;width:96px"><i></i></div>
      <span class="field-label" style="left:9px;top:166px">Keyword</span>
      <div class="text-input" style="left:8px;top:186px;width:205px">Beach Access</div>
      <div class="btn-dark" style="left:211px;top:186px;width:43px;height:29px;line-height:29px;border-radius:0 3px 3px 0">GO</div>
      <span class="small-link" style="left:9px;top:228px">Advanced Search</span>
    </section>

    <section class="abs box keep-in-touch">
      <h2 class="box-title">Keep In Touch</h2>
      <p class="intro">Newsletter with Deals &amp;<br>Local Knowledge To Your Inbox</p>
      <span class="field-label" style="left:7px;top:98px;font-size:15px">Name</span>
      <div class="text-input" style="left:56px;top:91px;width:199px"></div>
      <span class="field-label" style="left:8px;top:140px;font-size:15px">Email</span>
      <div class="text-input" style="left:56px;top:133px;width:199px"></div>
      <div class="social-btn">Socialnet<span></span></div>
      <div class="btn-dark" style="left:201px;top:175px;width:53px;height:29px;line-height:29px;font-size:15px">GO</div>
    </section>

    <section class="abs box deals">
      <h2 class="box-title">Deals</h2>
      <div class="deal-photo" role="img" aria-label="Photo of a couple relaxing on sun loungers by the sea"></div>
      <p class="deal-copy">Lorem ipsum Lorem ipsum dolor sit Lorem ipsum Lorem ipsum dolor sit Lorem Lorem ipsum</p>
      <span class="small-link" style="left:17px;top:189px;font-size:13.5px;font-weight:700">VIEW</span>
      <div class="btn-dark" style="left:201px;top:180px;width:53px;height:29px;line-height:29px;font-size:15px">View</div>
    </section>

    <div class="abs share-bar">
      <svg class="share-icon" style="left:12px" width="42" height="38" viewBox="0 0 42 38" aria-label="Email">
        <rect x="2" y="10" width="38" height="25" rx="2" fill="#f2f2f2" stroke="#777" stroke-width="1.5"/>
        <path d="M2 11 L21 25 L40 11 M2 34 L16 21 M40 34 L26 21" fill="none" stroke="#777" stroke-width="1.5"/>
      </svg>
      <div class="share-icon" style="left:72px;top:11px;width:34px;height:34px;background:#35b5ea;border-radius:4px"></div>
      <div class="share-icon" style="left:131px;top:10px;width:33px;height:33px;background:#3b5a98"></div>
      <span class="share-label">Share This</span>
    </div>
  </aside>

  <main>
    <div class="abs content"></div>
    <h1 class="abs welcome">Welcome to Tui Crib &amp; Seaside Cottages</h1>
    <p class="abs copy" style="left:364px;top:374px;width:484px">Lorem ipsum onsectetuer adipiscing elit, sed diam nonummy nibh euismod tincidunt ut laoreet dolore magna aliquam erat volutpat. Ut wisi enim ad minim veniam, quis nostrud exerci tation ullamcorper suscipit lobortis nisl ut aliquip ex ea commodo consequat.</p>
    <p class="abs copy" style="left:364px;top:458px;width:484px">Lorem ipsum onsectetuer adipiscing elit, sed diam nonummy nibh euismod tincidunt ut laoreet dolore magna aliquam erat volutpat. Ut wisi enim ad minim veniam, quis nostrud exerci tation ullamcorper suscipit lobortis nisl ut aliquip ex ea commodo consequat.</p>
    <p class="abs copy" style="left:364px;top:542px;width:484px">Lorem ipsum onsectetuer adipiscing elit, sed diam nonummy nibh euismod tincidunt ut laoreet dolore magna aliquam erat volutpat. Ut wisi enim ad minim veniam, quis nostrud exerci tation ullamcorper suscipit lobortis nisl ut aliquip ex ea commodo consequat.</p>

    <div class="abs shortlist">My<br>Shortlist</div>
    <div class="abs help">
      <h3>Help !</h3>
      <p>Can’t Find What You’re Looking For?<br>Contact Us For A Personal Property Search</p>
      <p class="phone">+64-27-555-0142</p>
    </div>

    <p class="abs copy" style="left:364px;top:638px;width:650px">Lorem ipsum onsectetuer adipiscing elit, sed diam nonummy nibh euismod tincidunt ut laoreet dolore magna aliquam erat volutpat. Ut wisi enim ad minim veniam, quis nostrud exerci tation ullamcorper suscipit lobortis nisl ut aliquip ex ea commodo consequat.</p>
    <p class="abs copy" style="left:364px;top:716px;width:650px">Lorem ipsum onsectetuer adipiscing elit, sed diam nonummy nibh euismod tincidunt ut laoreet dolore magna aliquam erat volutpat. Ut wisi enim ad minim veniam, quis nostrud exerci tation ullamcorper suscipit lobortis nisl ut aliquip ex ea commodo consequat.</p>

    <p class="abs cta">Just can’t find what you’re looking for?<br><a href="#">Contact us</a> for a personal property search.</p>

    <div class="abs feature-photo" style="left:358px;width:351px;background:linear-gradient(#1a2f5a,#3b4f78 35%,#d99a4a 60%,#2f6a6a 85%,#1f4a3c)" role="img" aria-label="Photo of a lit holiday villa beside a pool at dusk"></div>
    <div class="abs feature-photo" style="left:719px;width:293px;background:linear-gradient(#8fc3e8,#b9b39a 30%,#6fa35a 50%,#2bb4d6 70%,#4fc4dc)" role="img" aria-label="Photo of a tropical resort pool with thatched umbrellas and palms"></div>
    <span class="abs feature-label" style="left:358px;width:351px">Browse Homes</span>
    <span class="abs feature-label" style="left:719px;width:293px">Local Knowledge</span>
  </main>

  <footer>
    <div class="abs site-footer"></div>
    <div class="abs footer-links"><a href="#">Terms &amp; Conditions</a> <a href="#">Privacy Policy</a><a href="#">Contact Us List</a> <a href="#">Your Home</a></div>
  </footer>
</div>
</body>
</html>
```